FENNOX TAB (Disposable Charger) Needs packaging with actual mock up!

We have a word document with all the information that we need on the package so feel free to be creative and design your own. It is a small condom wrapper for a one-time use phone charger.

Below I have attached the file with the dimensions of the package. And also some competitors packaging for examples only. Please don't copy them. We need to be different and cooler.

Our logo is also below called Fennox Tab(See charger for logo we want). The other ones are just examples.

```html
<!DOCTYPE html>
<html lang="en">
<head>
<meta charset="utf-8">
<title>Fennox Tab – Disposable Charger Packaging</title>
<link rel="stylesheet" href="https://fonts.googleapis.com/css2?family=Audiowide&family=Russo+One&family=Poppins:ital,wght@0,500;1,400&family=Oswald:wght@400&display=swap">
<style>
  :root {
    --bg: #efeee9;
    --green-deep: #10301a;
    --green-dark: #18421f;
    --green-mid: #2e7431;
    --green-bright: #5fae46;
    --green-light: #72c46c;
    --lime: #d6e82c;
    --white: #ffffff;
    --silver: #d9dcd8;
  }
  * { box-sizing: border-box; margin: 0; padding: 0; }
  html, body { width: 1108px; height: 1200px; overflow: hidden; background: var(--bg); }
  .sheet { position: relative; width: 1108px; height: 1200px; }
  .dieline {
    position: absolute; left: 24px; top: 290px; width: 1060px; height: 620px;
    display: flex; box-shadow: 0 10px 30px rgba(0,0,0,.15);
  }
  .panel { position: relative; width: 530px; height: 620px; overflow: hidden; }
  .panel--front {
    background: radial-gradient(ellipse at 75% 60%, var(--green-mid) 0%, var(--green-dark) 45%, var(--green-deep) 100%);
  }
  .panel--back {
    background: linear-gradient(180deg, var(--green-deep) 0%, var(--green-dark) 35%, var(--green-mid) 75%, var(--green-bright) 100%);
  }

  .brand {
    position: absolute; left: 30px; top: 44px;
    font-family: "Audiowide", sans-serif; font-size: 21px; color: var(--green-light);
    letter-spacing: .5px; display: flex; align-items: center; gap: 7px; white-space: nowrap;
  }
  .brand__dot { width: 10px; height: 10px; border-radius: 50%; background: var(--green-light); }
  .hang-hole {
    position: absolute; left: 252px; top: 46px; width: 100px; height: 20px;
    background: var(--white); border-radius: 10px;
  }
  .hang-hole::before {
    content: ""; position: absolute; left: 39px; top: -8px; width: 22px; height: 16px;
    background: var(--white); border-radius: 11px 11px 0 0;
  }
  .compat {
    position: absolute; left: 366px; top: 25px; width: 138px; height: 70px;
    border: 2px solid var(--silver); border-radius: 8px;
    display: flex; align-items: center; justify-content: center; gap: 8px;
  }
  .compat__mark { width: 30px; height: 30px; background: var(--silver); border-radius: 50%; }
  .compat__mark--square { border-radius: 4px; background: var(--green-bright); }
  .compat__text {
    font-family: "Oswald", sans-serif; font-size: 11px; line-height: 1.35; color: var(--white);
    text-align: center; text-transform: uppercase;
  }

  .accent-band {
    position: absolute; left: -60px; top: 300px; width: 700px; height: 70px;
    background: linear-gradient(90deg, rgba(114,196,108,.55), rgba(114,196,108,.15) 70%, transparent);
    transform: rotate(-17deg); transform-origin: left top;
  }
  .headline {
    position: absolute; left: 40px; top: 175px; width: 420px;
    transform: rotate(-17deg); transform-origin: left top;
    font-family: "Russo One", sans-serif; font-style: italic; color: var(--white);
    text-transform: uppercase; line-height: .95;
  }
  .headline__small { font-size: 38px; display: block; }
  .headline__big { font-size: 60px; display: block; color: var(--silver); }
  .headline__url {
    display: block; margin-top: 10px; font-size: 21px; color: var(--lime); letter-spacing: .5px;
  }
  .product-shot {
    position: absolute; left: 355px; top: 250px; width: 150px; height: 290px;
    border-radius: 14px;
    background: radial-gradient(ellipse at 50% 70%, #f3f6f2 0%, #cde8c6 40%, rgba(95,174,70,.35) 75%, transparent 100%);
  }
  .seal {
    position: absolute; left: 45px; top: 440px; width: 88px; height: 88px; border-radius: 50%;
    background: var(--green-bright); border: 4px solid var(--silver);
  }
  .capacity {
    position: absolute; left: 42px; top: 540px;
    font-family: "Audiowide", sans-serif; color: var(--white); line-height: 1.15;
  }
  .capacity__mah { font-size: 24px; display: block; }
  .capacity__status { font-size: 21px; display: block; }
  .capacity__status em { font-style: normal; color: var(--lime); }

  .stopwatch {
    position: absolute; left: 55px; top: 120px; width: 125px; height: 125px; border-radius: 50%;
    background: radial-gradient(circle, var(--white) 0%, var(--lime) 45%, var(--green-bright) 75%, var(--green-mid) 100%);
  }
  .talk {
    position: absolute; left: 186px; top: 150px;
    font-family: "Russo One", sans-serif; font-style: italic; text-transform: uppercase; line-height: 1;
  }
  .talk__hours { display: block; font-size: 44px; color: var(--white); }
  .talk__sub { display: block; font-size: 28px; color: var(--lime); margin-top: 2px; }

  .directions-bar {
    position: absolute; left: 52px; top: 263px; width: 290px; height: 28px;
    background: linear-gradient(90deg, var(--green-bright), rgba(95,174,70,0));
    font-family: "Audiowide", sans-serif; font-size: 16px; color: var(--white);
    padding: 4px 8px; letter-spacing: .5px;
  }
  .directions {
    position: absolute; left: 56px; top: 308px; width: 450px;
    font-family: "Poppins", sans-serif; font-weight: 500; font-size: 12px; line-height: 1.7; color: var(--white);
    list-style: none;
  }
  .directions li { margin-bottom: 5px; }
  .directions .sub { display: block; padding-left: 16px; }
  .caution {
    position: absolute; left: 56px; top: 465px; width: 450px;
    font-family: "Poppins", sans-serif; font-style: italic; font-size: 10.5px; color: var(--silver);
  }
  .specs {
    position: absolute; left: 56px; top: 522px;
    font-family: "Poppins", sans-serif; font-weight: 500; font-size: 12px; color: var(--white);
  }
  .cert-row { position: absolute; left: 56px; top: 548px; display: flex; gap: 6px; }
  .cert-row span { width: 16px; height: 16px; border: 2px solid var(--white); border-radius: 50%; }
  .cert-row span:nth-child(even) { border-radius: 2px; }
  .upc-space {
    position: absolute; left: 355px; top: 517px; width: 146px; height: 75px; background: var(--white);
  }
</style>
</head>
<body>
<main class="sheet">
  <section class="dieline">

    <article class="panel panel--front">
      <div class="brand"><span class="brand__dot"></span>FENNOX TAB</div>
      <div class="hang-hole"></div>
      <div class="compat">
        <span class="compat__mark"></span>
        <span class="compat__text">Compatible<br>with<br>both</span>
        <span class="compat__mark compat__mark--square"></span>
      </div>

      <div class="accent-band"></div>
      <h1 class="headline">
        <span class="headline__small">Disposable</span>
        <span class="headline__small">Cell Phone</span>
        <span class="headline__big">Charger</span>
        <span class="headline__url">www.fennox-tab.com</span>
      </h1>

      <div class="product-shot" role="img" aria-label="White charger pod with attached cable, glowing with green electric light"></div>
      <div class="seal" role="img" aria-label="Biodegradable badge"></div>

      <p class="capacity">
        <span class="capacity__mah">2900mah</span>
        <span class="capacity__status">CHARGED UP <em>Ready for use</em></span>
      </p>
    </article>

    <article class="panel panel--back">
      <div class="brand"><span class="brand__dot"></span>FENNOX TAB</div>
      <div class="hang-hole"></div>
      <div class="compat">
        <span class="compat__mark"></span>
        <span class="compat__text">Compatible<br>with<br>both</span>
        <span class="compat__mark compat__mark--square"></span>
      </div>

      <div class="stopwatch" role="img" aria-label="Stopwatch with lightning bolt illustration"></div>
      <h2 class="talk">
        <span class="talk__hours">8 Hours</span>
        <span class="talk__sub">Of Talk Time</span>
      </h2>

      <div class="directions-bar">DIRECTIONS</div>
      <ol class="directions">
        <li>1.&nbsp; Plug into your device and switch on pod.
          <span class="sub">(For maximum charge, close all open apps)</span></li>
        <li>2.&nbsp; Pod will charge until light shuts off, or turn off for future use.</li>
        <li>3.&nbsp; Please recycle battery, the shell is biodegradable
          <span class="sub">- Total charge varies by device</span>
          <span class="sub">- UPC code Space (BOTTOM RIGHT)</span></li>
      </ol>
      <p class="caution">*Caution: Don't get pod wet. Do not disassemble device. Battery may get warm.</p>

      <p class="specs">2900mAh Output 5V 1000ma</p>
      <div class="cert-row" aria-label="Certification marks">
        <span></span><span></span><span></span><span></span><span></span><span></span><span></span>
      </div>
      <div class="upc-space"></div>
    </article>

  </section>
</main>
</body>
</html>
```